The Plasterline & Soundcraft Partners Inc (PSPI)

Create a LOGO and Business Card design.

Colors: Black, Bright Yellow & Red

Description of company: commercial carpentry, metal framing, drywall, taping/spackling, demolition, rough/finish carpentry.

Target Market(s)

developers, architects, general contractors, construction managers

Industry/Entity Type

Business

```html
<!DOCTYPE html>
<html lang="en">
<head>
<meta charset="utf-8">
<title>PSPI Business Card</title>
<link rel="stylesheet" href="https://fonts.googleapis.com/css2?family=Questrial&family=Tinos&display=swap">
<style>
  :root {
    --page: #ffffff;
    --card: #000000;
    --accent: #d50f0f;
    --ink: #ffffff;
  }
  * { box-sizing: border-box; margin: 0; padding: 0; }
  html, body {
    width: 1200px; height: 900px; overflow: hidden;
    background: var(--page);
    font-family: "Questrial", "Century Gothic", sans-serif;
  }
  .canvas { position: relative; width: 1200px; height: 900px; }

  .card {
    position: absolute;
    width: 620px; height: 380px;
    background: var(--card);
    border-radius: 16px;
    overflow: hidden;
  }

  /* front */
  .card--front { left: 90px; top: 70px; }
  .side-bar {
    position: absolute; width: 16px; height: 140px;
    background: var(--accent);
  }
  .side-bar--left { left: 36px; top: 210px; }
  .side-bar--right { right: 24px; top: 110px; }
  .front-brand {
    position: absolute; left: 0; right: 0; top: 130px;
    text-align: center; color: var(--ink);
  }
  .wordmark {
    display: inline-flex; align-items: center; gap: 18px;
    font-size: 92px; letter-spacing: 34px; line-height: 1;
    color: var(--ink);
  }
  .wordmark__mark {
    width: 18px; height: 18px; background: var(--accent); flex: none;
  }
  .tagline {
    margin-top: 18px; font-size: 17px; letter-spacing: 0.3px;
  }

  /* back */
  .card--back { left: 490px; top: 470px; }
  .band {
    position: absolute; left: 0; right: 0; height: 26px;
    background: var(--accent);
  }
  .band--top { top: 0; }
  .band--bottom { bottom: 0; }
  .back-brand {
    position: absolute; left: 48px; top: 138px; color: var(--ink);
  }
  .back-brand .wordmark { font-size: 50px; letter-spacing: 20px; gap: 10px; }
  .back-brand .wordmark__mark { width: 11px; height: 11px; }
  .back-brand .tagline { margin-top: 10px; font-size: 10.5px; }

  .person { position: absolute; left: 370px; top: 118px; color: var(--accent); }
  .person__name { font-family: "Tinos", "Times New Roman", serif; font-size: 22px; line-height: 1.1; }
  .person__role { font-size: 18px; }

  .contacts {
    position: absolute; left: 362px; top: 190px;
    list-style: none; color: var(--ink); font-size: 13px;
  }
  .contacts li { display: flex; align-items: center; height: 19px; }
  .contacts svg { width: 14px; height: 14px; margin-right: 18px; fill: var(--accent); flex: none; }
</style>
</head>
<body>
<main class="canvas">

  <section class="card card--front" aria-label="Card front">
    <div class="side-bar side-bar--left"></div>
    <div class="side-bar side-bar--right"></div>
    <div class="front-brand">
      <div class="wordmark"><span class="wordmark__mark"></span>PSPI</div>
      <p class="tagline">Plasterline &amp; Soundcraft Partners Incorporated</p>
    </div>
  </section>

  <section class="card card--back" aria-label="Card back">
    <div class="band band--top"></div>
    <div class="band band--bottom"></div>

    <div class="back-brand">
      <div class="wordmark"><span class="wordmark__mark"></span>PSPI</div>
      <p class="tagline">Plasterline &amp; Soundcraft Partners Incorporated</p>
    </div>

    <div class="person">
      <p class="person__name">Marcus Hale</p>
      <p class="person__role">Director</p>
    </div>

    <ul class="contacts">
      <li><svg viewBox="0 0 16 16"><path d="M2 6c0-2 2-3 6-3s6 1 6 3l-3 1-1-2H6L5 7zM3 8h10l1 6H2z"/></svg>xxxx-xxxx</li>
      <li><svg viewBox="0 0 16 16"><path d="M8 1l7 7h-2v7H9v-4H7v4H3V8H1z"/></svg>48 Mill Lane, Harbor City</li>
      <li><svg viewBox="0 0 16 16"><path d="M5 1h6a1 1 0 0 1 1 1v12a1 1 0 0 1-1 1H5a1 1 0 0 1-1-1V2a1 1 0 0 1 1-1zm0 2v9h6V3z"/></svg>xxxx-xxxx</li>
      <li><svg viewBox="0 0 16 16"><path d="M1 3h14v10H1zm1 1.5V12h12V4.5L8 9z"/></svg>m.hale@pspi.com</li>
      <li><svg viewBox="0 0 16 16"><path d="M8 1a7 7 0 1 0 0 14A7 7 0 0 0 8 1zm0 1.2c.9.9 1.6 2.3 1.8 3.8H6.2C6.4 4.5 7.1 3.1 8 2.2zM2.3 7h2.9c0 .7 0 1.4.1 2H2.3a5.8 5.8 0 0 1 0-2zm8.5 0h2.9a5.8 5.8 0 0 1 0 2h-2.9c.1-.6.1-1.3 0-2zm-4.6 0h3.6c.1.7.1 1.4 0 2H6.2c-.1-.6-.1-1.3 0-2zm0 3h3.6c-.2 1.5-.9 2.9-1.8 3.8-.9-.9-1.6-2.3-1.8-3.8z"/></svg>www.pspi.com</li>
    </ul>
  </section>

</main>
</body>
</html>
```